UPT online New Year's greeting card**

We would like to send an original digital New year's card via Email to all our customers. We are a company located in Belgium (Europe). We load and unload new cars from Roll-on-Roll-off vessels. More info can be found on our website: www.uptterminals.example

```html
<!DOCTYPE html>
<html lang="en">
<head>
<meta charset="utf-8">
<title>UPT – Happy New Year</title>
<link rel="stylesheet" href="https://fonts.googleapis.com/css2?family=Kaushan+Script&family=Marck+Script&family=Roboto+Condensed:wght@400&display=block">
<style>
  :root {
    --royal: #0a3db5;
    --royal-deep: #0634a8;
    --ink-blue: #0c3aa8;
    --cyan-soft: #8fe9f7;
    --band: #c9f7f6;
    --card: #ffffff;
    --text-dark: #111111;
  }
  * { margin: 0; padding: 0; box-sizing: border-box; }
  html, body { width: 1200px; height: 891px; overflow: hidden; background: var(--royal); }
  .greeting-card {
    position: relative;
    width: 1200px;
    height: 891px;
    overflow: hidden;
    background: linear-gradient(90deg, var(--royal-deep) 0%, #2a5cc6 22%, #6f97de 27%, #2a5cc6 73%, var(--royal-deep) 100%);
  }
  .side-mandala {
    position: absolute;
    top: 10px;
    width: 580px;
    height: 870px;
    border-radius: 50%;
    background: radial-gradient(circle, #3f9fe2 0%, #2fb4ea 35%, #46b8ea 55%, #3b7fd8 80%, rgba(10,61,181,0) 100%);
    opacity: 0.9;
  }
  .side-mandala--left { left: 10px; }
  .side-mandala--right { left: 605px; }
  .center-band {
    position: absolute;
    left: 325px;
    top: 0;
    width: 551px;
    height: 891px;
    background: var(--band);
  }
  .card-panel {
    position: absolute;
    left: 351px;
    top: 29px;
    width: 501px;
    height: 832px;
    background: var(--card);
  }
  .ornament {
    position: absolute;
    left: 516px;
    width: 170px;
    height: 96px;
    background: radial-gradient(ellipse at center, var(--cyan-soft) 0%, #b9f3fb 55%, rgba(255,255,255,0) 75%);
  }
  .ornament--top { top: 29px; }
  .ornament--bottom { top: 767px; }
  .thanks-message {
    position: absolute;
    left: 351px;
    top: 143px;
    width: 501px;
    text-align: center;
    font-family: "Marck Script", cursive;
    font-size: 29px;
    font-weight: 400;
    line-height: 38px;
    color: var(--ink-blue);
  }
  .headline { font-weight: 400; }
  .headline-word {
    position: absolute;
    display: inline-block;
    font-family: "Kaushan Script", cursive;
    font-weight: 400;
    color: var(--ink-blue);
    font-size: 80px;
    line-height: 1;
    transform: rotate(-8deg);
    white-space: nowrap;
  }
  .headline-word--happy { left: 474px; top: 335px; }
  .headline-word--new { left: 540px; top: 420px; }
  .headline-word--year { left: 552px; top: 512px; }
  .divider {
    position: absolute;
    left: 351px;
    width: 501px;
    height: 3px;
    background: linear-gradient(90deg, rgba(12,58,168,0) 0%, var(--ink-blue) 15%, var(--ink-blue) 85%, rgba(12,58,168,0) 100%);
  }
  .divider--upper { top: 652px; }
  .divider--lower { top: 756px; }
  .brand {
    position: absolute;
    left: 372px;
    top: 683px;
    display: flex;
    align-items: center;
    gap: 12px;
  }
  .brand-dot {
    width: 44px;
    height: 44px;
    border-radius: 50%;
    background: var(--ink-blue);
  }
  .brand-name {
    font-family: "Roboto Condensed", sans-serif;
    font-size: 40px;
    color: var(--ink-blue);
    letter-spacing: 1px;
  }
  .website {
    position: absolute;
    left: 560px;
    top: 699px;
    width: 280px;
    text-align: right;
    font-family: "Roboto Condensed", sans-serif;
    font-size: 22px;
    line-height: 28px;
    color: var(--text-dark);
    white-space: nowrap;
  }
</style>
</head>
<body>
  <main class="greeting-card">
    <div class="side-mandala side-mandala--left" role="img" aria-label="Blue and cyan mandala ornament"></div>
    <div class="side-mandala side-mandala--right" role="img" aria-label="Blue and cyan mandala ornament"></div>
    <div class="center-band"></div>
    <div class="card-panel"></div>
    <div class="ornament ornament--top" role="img" aria-label="Cyan lace ornament"></div>
    <p class="thanks-message">Thank you so much for supporting<br>business in 2019.<br>We're looking forward to<br>serving you again in 2020!</p>
    <h1 class="headline">
      <span class="headline-word headline-word--happy">Happy</span>
      <span class="headline-word headline-word--new">New</span>
      <span class="headline-word headline-word--year">Year</span>
    </h1>
    <div class="divider divider--upper"></div>
    <div class="brand">
      <span class="brand-dot"></span>
      <span class="brand-name">UPT</span>
    </div>
    <p class="website">www.uptterminals.example</p>
    <div class="divider divider--lower"></div>
    <div class="ornament ornament--bottom" role="img" aria-label="Cyan lace ornament"></div>
  </main>
</body>
</html>
```